Business card and stationary for consulting business

We need business cards and matching stationary for professional consulting business for employment and human resources issues.
One of the CraftHive designers designed the logo with our company name.  Use the colors in the logo and may use light yellow as an accent color.
Add
Mara T. Vollen, J.D., LL.M.
485 E. Callister Lane
Winter Park, Florida  32789
407-555-0183
maravollenjd@quillpost.example

Industry/Entity Type
Business

```html
<!DOCTYPE html>
<html lang="en">
<head>
<meta charset="utf-8">
<title>Northlane HR — Business Card</title>
<link rel="stylesheet" href="https://fonts.googleapis.com/css2?family=Arimo:wght@400&family=Montserrat:wght@400&display=swap">
<style>
  :root {
    --band-top: #0080b0;
    --paper: #ffffff;
    --blue-deep: #008fc8;
    --blue-bright: #00abeb;
    --brand-teal: #1d6f8e;
    --divider: #c9cdd0;
    --text-light: #ffffff;
  }
  html, body {
    margin: 0;
    padding: 0;
    overflow: hidden;
    background: #ffffff;
  }
  .card {
    position: relative;
    width: 1200px;
    height: 686px;
    overflow: hidden;
    font-family: "Arimo", Arial, sans-serif;
  }
  .top-band {
    position: absolute;
    left: 0; top: 0;
    width: 100%; height: 43px;
    background: var(--band-top);
  }
  .brand-strip {
    position: absolute;
    left: 0; top: 43px;
    width: 100%; height: 214px;
    background: var(--paper);
  }
  .brand-name {
    position: absolute;
    right: 537px;
    top: 78px;
    margin: 0;
    font-family: "Montserrat", Arial, sans-serif;
    font-weight: 400;
    font-size: 66px;
    line-height: 1;
    letter-spacing: -0.5px;
    color: var(--brand-teal);
    white-space: nowrap;
  }
  .brand-divider {
    position: absolute;
    left: 681px;
    top: 29px;
    width: 3px;
    height: 157px;
    background: var(--divider);
  }
  .tagline {
    position: absolute;
    left: 703px;
    top: 57px;
    margin: 0;
    padding: 0;
    list-style: none;
    font-family: "Montserrat", Arial, sans-serif;
    font-weight: 400;
    font-size: 26px;
    line-height: 34px;
    color: var(--brand-teal);
  }
  .contact-panel {
    position: absolute;
    left: 0; top: 257px;
    width: 100%; height: 429px;
    background: linear-gradient(180deg, var(--blue-deep) 0%, var(--blue-bright) 100%);
    color: var(--text-light);
    text-align: center;
  }
  .person-name {
    position: absolute;
    left: 0; right: 0;
    top: 65px;
    margin: 0;
    font-weight: 400;
    font-size: 43px;
    line-height: 1;
    letter-spacing: 0.5px;
  }
  .address {
    position: absolute;
    left: 0; right: 0;
    top: 120px;
    margin: 0;
    font-style: normal;
    font-size: 33px;
    line-height: 41px;
  }
  .phone {
    position: absolute;
    left: 0; right: 0;
    top: 250px;
    margin: 0;
    font-size: 33px;
    line-height: 1;
  }
  .email {
    position: absolute;
    left: 0; right: 0;
    top: 334px;
    margin: 0;
    font-size: 33px;
    line-height: 1;
  }
</style>
</head>
<body>
  <div class="card">
    <div class="top-band"></div>

    <header class="brand-strip">
      <p class="brand-name">Northlane HR</p>
      <div class="brand-divider"></div>
      <ul class="tagline">
        <li>Grow Revenue</li>
        <li>Steady Budgets</li>
        <li>Guard Margins</li>
      </ul>
    </header>

    <section class="contact-panel">
      <h1 class="person-name">MARA T. VOLLEN, J.D., LL.M.</h1>
      <address class="address">
        485 E. Callister Lane<br>
        Larkspur Bay, Oregon 97412
      </address>
      <p class="phone">407-555-0183</p>
      <p class="email">maravollenjd@quillpost.example</p>
    </section>
  </div>
</body>
</html>
```